Wrap on a Dravo truck with a topper the focus is Roofing.
The company name Pellick Construction, I have attached a business card.
I have attached their current bill board in town that should have all the info you need to design the wrap. I have also attached picture of the truck

```html
<!DOCTYPE html>
<html lang="en">
<head>
<meta charset="utf-8">
<title>Pellick Construction – Truck Wrap</title>
<link rel="stylesheet" href="https://fonts.googleapis.com/css2?family=Montserrat:wght@600;700;800&display=swap">
<style>
  :root {
    --canvas-grey: #7b7b7b;
    --wrap-black: #0d0d0d;
    --wrap-charcoal: #2a2a2a;
    --accent-red: #e8201f;
    --ink-white: #ffffff;
    --window-grey: #7b7b7b;
    --trim-grey: #4a4a4a;
    --house-light: #8d8d8d;
    --house-dark: #3a3a3a;
  }
  html, body {
    margin: 0;
    padding: 0;
    width: 943px;
    height: 1200px;
    overflow: hidden;
    background: var(--canvas-grey);
  }
  .wrap-canvas {
    width: 943px;
    height: 1200px;
    display: flex;
    align-items: center;
    justify-content: center;
  }
  .wrap-layout {
    width: 943px;
    height: auto;
    display: block;
  }
  .brand-text {
    font-family: "Montserrat", Arial, sans-serif;
  }
  .headline { fill: var(--accent-red); font-weight: 800; font-size: 62px; letter-spacing: -1px; }
  .phone { fill: var(--ink-white); font-weight: 700; font-size: 32px; letter-spacing: 1px; }
  .tagline { fill: var(--ink-white); font-weight: 700; font-size: 24px; }
  .tagline-small { fill: var(--ink-white); font-weight: 700; font-size: 11px; }
  .company-name { fill: var(--ink-white); font-weight: 800; font-size: 66px; }
  .company-sub { fill: var(--ink-white); font-weight: 700; font-size: 38px; }
  .services { fill: var(--accent-red); font-weight: 700; font-size: 16px; }
  .logo-word { fill: var(--ink-white); font-weight: 800; font-size: 44px; }
  .red-band { fill: var(--accent-red); }
  .vehicle-body { fill: var(--wrap-black); }
  .glass { fill: var(--window-grey); }
  .topper-seam { stroke: var(--trim-grey); stroke-width: 3; fill: none; }
  .latch { fill: var(--trim-grey); }
</style>
</head>
<body>
<main class="wrap-canvas">
  <svg class="wrap-layout" viewBox="0 0 1708 540" xmlns="http://www.w3.org/2000/svg" role="group" aria-label="Pellick Construction pickup and topper side wrap">
    <defs>
      <linearGradient id="houseTone" x1="0" y1="0" x2="0" y2="1">
        <stop offset="0" stop-color="var(--house-dark)"/>
        <stop offset="0.5" stop-color="var(--house-light)"/>
        <stop offset="1" stop-color="var(--house-dark)"/>
      </linearGradient>
      <linearGradient id="bodySheen" x1="0" y1="0" x2="0" y2="1">
        <stop offset="0" stop-color="#1c1c1c"/>
        <stop offset="1" stop-color="#050505"/>
      </linearGradient>
    </defs>

    <!-- vehicle silhouette -->
    <path class="vehicle-body" fill="url(#bodySheen)"
      d="M35,280 L70,250 L240,222 L236,238 L400,226 L460,172 L560,102 L940,97 L945,85 L1600,85 L1612,100 L1612,238 L1625,252 L1622,375 L1590,378 L1590,470
         L1455,470 L1450,400 Q1440,330 1330,330 Q1220,330 1200,400 L1195,470
         L360,470 L350,362 Q330,335 230,335 Q130,335 112,362 L40,362 Z"/>

    <!-- glass -->
    <path class="glass" d="M462,200 L560,122 Q580,118 700,118 L705,120 L705,240 L470,240 Z"/>
    <rect class="glass" x="745" y="118" width="120" height="128" rx="14"/>

    <!-- topper details -->
    <line class="topper-seam" x1="948" y1="120" x2="1608" y2="120"/>
    <rect class="latch" x="1122" y="195" width="36" height="22" rx="3"/>
    <rect class="latch" x="1425" y="195" width="36" height="22" rx="3"/>

    <!-- house photo area -->
    <path role="img" aria-label="Photo of a brick house with grey shingle roof under a stormy sky"
      fill="url(#houseTone)" opacity="0.85"
      d="M1015,470 L1015,400 L1040,330 L1110,290 L1200,292 L1240,250 L1300,250 L1420,310 L1500,320 L1560,400 L1545,470 L1455,470 L1450,400 Q1440,330 1330,330 Q1220,330 1200,400 L1195,470 Z"/>

    <!-- red information bands -->
    <polygon class="red-band" points="965,237 1215,237 1185,292 992,292"/>
    <polygon class="red-band" points="1300,237 1622,237 1626,280 1330,280"/>

    <!-- headline -->
    <text class="brand-text headline" x="975" y="178">NEED A NEW ROOF?</text>

    <!-- contact line -->
    <text class="brand-text phone" x="978" y="268">555.014.2270</text>
    <text class="brand-text tagline" x="1335" y="258">Storm Damage Experts</text>
    <text class="brand-text tagline-small" x="1417" y="276">LICENSED INSURED &amp; LOCAL</text>

    <!-- brand mark placement -->
    <text class="brand-text logo-word" x="895" y="370" text-anchor="middle">PELLICK</text>

    <!-- company name block -->
    <text class="brand-text company-name" x="582" y="360" text-anchor="middle">PELLICK</text>
    <text class="brand-text company-sub" x="582" y="407" text-anchor="middle">CONSTRUCTION</text>
    <text class="brand-text services" x="582" y="447" text-anchor="middle">ROOFING • SIDING • GUTTERS • PAINTING</text>
  </svg>
</main>
</body>
</html>
```